Commercial Landscaping Flyer Needed

Looking for a flyer design to showcase what we offer for commercial landscape Installations. We want this to illustrate what sets us apart from our competitors. Include our EMR Safety rating of .72, that our average commercial landscape installation size is $215,000 with our largest completed in 2020 being $1,375,590. We have backgrounds in commercial design and installation and help our customers with Value Engineering Strategies. Since incorporating in 2005, we have an average employment retention length of 8 years. We want this flyer to show our commercial clients that we mean business and are dedicated to making their project happen on time, run efficiently, and we do excellent work.

Need extra days to review

```html
<!DOCTYPE html>
<html lang="en">
<head>
<meta charset="utf-8">
<title>Fieldline Works Inc. – Commercial Landscape Installations</title>
<link href="https://fonts.googleapis.com/css2?family=Baloo+2:wght@500;600;700&display=swap" rel="stylesheet">
<style>
  :root {
    --paper: #f4f4f4;
    --paper-shade: #e2e2e2;
    --lime: #c3d82e;
    --lime-deep: #9fbb1c;
    --ink: #111111;
    --white: #ffffff;
    --band: #000000;
  }
  * { margin: 0; padding: 0; box-sizing: border-box; }
  html, body {
    width: 849px;
    height: 1200px;
    overflow: hidden;
    background: var(--paper);
  }
  .flyer {
    position: relative;
    width: 849px;
    height: 1200px;
    overflow: hidden;
    font-family: "Baloo 2", "Trebuchet MS", sans-serif;
    color: var(--ink);
    background: radial-gradient(circle at 280px 140px, #ffffff 0, var(--paper) 260px, var(--paper-shade) 620px, var(--paper) 900px);
  }
  .artwork {
    position: absolute;
    inset: 0;
    width: 849px;
    height: 1200px;
  }
  .brand {
    position: absolute;
    left: 62px;
    top: 122px;
    display: flex;
    align-items: center;
    gap: 12px;
  }
  .brand-dot {
    width: 34px;
    height: 34px;
    border-radius: 50%;
    background: var(--lime);
  }
  .brand-name {
    font-size: 38px;
    font-weight: 700;
    line-height: 1;
    color: var(--ink);
  }
  .stat {
    position: absolute;
    line-height: 1;
  }
  .stat-label {
    font-size: 27px;
    font-weight: 600;
    line-height: 27px;
  }
  .stat-value {
    font-weight: 600;
    letter-spacing: -1px;
  }
  .stat--safety {
    right: 30px;
    top: 148px;
    text-align: right;
  }
  .stat--safety .stat-label { font-size: 30px; line-height: 32px; }
  .stat--safety .stat-value { font-size: 94px; line-height: 80px; }
  .stat--largest {
    left: 61px;
    top: 916px;
  }
  .stat--average {
    right: 41px;
    top: 916px;
    text-align: right;
  }
  .stat--largest .stat-value { font-size: 75px; line-height: 70px; }
  .stat--average .stat-value { font-size: 73px; line-height: 70px; }
  .contact {
    position: absolute;
    left: 0;
    right: 0;
    top: 1112px;
    text-align: center;
    color: var(--white);
    font-size: 34px;
    font-weight: 600;
    line-height: 35px;
  }
</style>
</head>
<body>
<main class="flyer">
  <svg class="artwork" viewBox="0 0 849 1200" xmlns="http://www.w3.org/2000/svg">
    <defs>
      <linearGradient id="lime-tint" x1="0" y1="0" x2="1" y2="1">
        <stop offset="0" stop-color="#d2e24a"/>
        <stop offset="0.5" stop-color="#b8cf2a"/>
        <stop offset="1" stop-color="#9fbb1c"/>
      </linearGradient>
      <linearGradient id="courtyard" x1="0.2" y1="0" x2="0.8" y2="1">
        <stop offset="0" stop-color="#7c766e"/>
        <stop offset="0.3" stop-color="#9a9386"/>
        <stop offset="0.55" stop-color="#c9c8bf"/>
        <stop offset="0.75" stop-color="#b58c78"/>
        <stop offset="1" stop-color="#6a9a45"/>
      </linearGradient>
    </defs>

    <g class="backdrop-arcs" fill="none" stroke="#ffffff" stroke-width="14" opacity="0.5">
      <circle cx="280" cy="240" r="260"/>
      <circle cx="280" cy="240" r="420"/>
      <circle cx="280" cy="240" r="580"/>
    </g>

    <g class="site-photos" role="img" aria-label="Lime-tinted photographs of apartment buildings and a finished landscaped rooftop">
      <circle cx="575" cy="303" r="200" fill="url(#lime-tint)"/>
      <circle cx="209" cy="484" r="189" fill="url(#lime-tint)"/>
      <circle cx="205" cy="866" r="180" fill="url(#lime-tint)"/>
      <circle cx="388" cy="964" r="96" fill="url(#lime-tint)"/>
      <circle cx="645" cy="878" r="192" fill="url(#lime-tint)"/>
    </g>

    <g class="photo-rings" fill="none" stroke="var(--white)" stroke-width="2" stroke-linecap="round">
      <path d="M430 198 A165 165 0 1 1 615 490"/>
      <path d="M66 520 A165 165 0 0 1 330 346"/>
      <path d="M82 750 A165 165 0 0 0 280 1005"/>
      <path d="M700 725 A165 165 0 0 1 540 1030"/>
      <path d="M315 1010 A60 60 0 0 1 340 870"/>
    </g>

    <circle cx="430" cy="624" r="268" fill="#e8e8e8"/>
    <circle class="feature-photo" cx="430" cy="624" r="258" fill="url(#courtyard)"
            role="img" aria-label="Aerial photograph of a completed rooftop courtyard with lawn, paving, planters and seating"/>
    <g class="feature-ring" fill="none" stroke="var(--white)" stroke-width="2.5" stroke-linecap="round">
      <path d="M395 390 A237 237 0 1 0 395 858"/>
      <path d="M455 388 A237 237 0 1 1 455 860"/>
    </g>

    <path class="footer-accent" d="M0 1125 Q424 1080 849 1125 L849 1200 L0 1200 Z" fill="var(--lime)"/>
    <path class="footer-band" d="M0 1133 Q424 1092 849 1133 L849 1200 L0 1200 Z" fill="var(--band)"/>
  </svg>

  <header class="brand">
    <span class="brand-dot"></span>
    <span class="brand-name">Fieldline Works Inc.</span>
  </header>

  <section class="stat stat--safety">
    <p class="stat-label">EMR Safety rating of</p>
    <p class="stat-value">.72</p>
  </section>

  <section class="stat stat--largest">
    <p class="stat-label">largest completed<br>in 2020 being</p>
    <p class="stat-value">$1,375,590</p>
  </section>

  <section class="stat stat--average">
    <p class="stat-label">average commercial landscape<br>installation size</p>
    <p class="stat-value">$215,000</p>
  </section>

  <footer class="contact">
    <p>call us : 012345678</p>
    <p>www. yourwebsite.com</p>
  </footer>
</main>
</body>
</html>
```